Fitness Equipment & Service

I want to make the card eye catching and fun. We are called Corvane Motion Limited and we are based in Wales. We sell, install and service all types of fitness equipment from Skipping ropes, right through the Dumbbells, Kettle bells and Barbells through to state of the art Treadmills, Running Machines and Strength Equipment. We also design and install changing room furniture and lockers.

TYPOGRAPHY
We would like to use Futrura. Futura has an appearance of efficiency and forwardness. The typeface is derived
from simple geometric forms (near-perfect circles, triangles and squares) and is based on strokes of
near-even weight, which are low in contrast. This is most visible in the almost perfectly round stroke of
the o, which is nonetheless slightly ovoid.
The lowercase has tall ascenders, which rise above the cap line. The uppercase
characters present proportions similar to those of classical Roman capitals.

TYPOGRAPHIC CONSIDERATIONS
No Strike though
No Horizontal Scaling
No Drop Shadows
No Effects
Never use less than 120% Leading

OUR CORPORATE COLOURS
BRAND GUIDELINES
We were thinking that our primary colour palette consists of the Acid Green (Pantone 382) and Process Black.

We work closely with tolbrook Ltd and would like to include their name on the card somewhere. I have attached images of the other brands that we work with as an idea or the small icons I have included that illustrate what we do?. I have very kindly been given permission to use any of the images off the files that I have included below, so I hope these help. I will include these below. I would be open to suggestions if it made the card more striking Can you do it?
Updates

Hi All, Just wanted to add a few thoughts but you are the guys with the creative visions (thats why are here) We are based in Wales, UK and we would be open to lots of different ideas on a theme but must be eye catching, Bold and FUN. If you can or think that the Welsh or any dragon could be put in there then go for it (its not a must have) We have also added some ideas for colour but again its over to you!! GO FOR IT ! Thanks and look forward to your visions! Owen

Hi All, Just thought I would sen through the contact details that need to be on the card. (if you want to play around with icons instead of the wording twitter, Facebook, go for it): Corvane Motion Limited Owen Pritchard Managing Director Mob: +44 (0)7382 519 046 e-mail: sales@corvanemotion.co.uk Web: Corvanemotion.co.uk twitter: @motionPostbag Facebook: Corvane Motion Limited

Industry/Entity Type

Fitness

```html
<!DOCTYPE html>
<html lang="en">
<head>
<meta charset="utf-8">
<title>Corvane Motion Limited – Business Card</title>
<link href="https://fonts.googleapis.com/css2?family=Jost:wght@400;500&display=swap" rel="stylesheet">
<style>
  :root {
    --backdrop: #8f9092;
    --card-blue-top: #2265ad;
    --card-blue-mid: #17428a;
    --card-blue-bottom: #0e1a4f;
    --gold: #f0b93a;
    --icon-gold: #e2ad3a;
    --white: #ffffff;
    --navy: #151a48;
  }
  html, body {
    margin: 0;
    padding: 0;
    width: 1105px;
    height: 1200px;
    overflow: hidden;
    background: var(--backdrop);
    font-family: "Jost", "Futura", sans-serif;
  }
  .canvas {
    position: relative;
    width: 1105px;
    height: 1200px;
  }
  .card {
    position: absolute;
    left: 184px;
    width: 744px;
    height: 424px;
    box-sizing: border-box;
  }
  .card-front {
    top: 120px;
    background: linear-gradient(180deg, var(--card-blue-top) 0%, var(--card-blue-mid) 55%, var(--card-blue-bottom) 100%);
    border: 2px solid #0a1236;
    color: var(--white);
    overflow: hidden;
  }
  .world-map {
    position: absolute;
    inset: 0;
    background: radial-gradient(ellipse at 45% 30%, rgba(90,150,215,0.25) 0%, rgba(90,150,215,0) 65%);
  }
  .holder-name {
    position: absolute;
    left: 32px;
    top: 26px;
    margin: 0;
    font-size: 33px;
    font-weight: 500;
    line-height: 1.2;
    color: var(--gold);
  }
  .holder-title {
    position: absolute;
    left: 32px;
    top: 66px;
    margin: 0;
    font-size: 24px;
    font-weight: 400;
    line-height: 1.2;
  }
  .address {
    position: absolute;
    left: 32px;
    top: 190px;
    margin: 0;
    font-style: normal;
    font-size: 19.5px;
    line-height: 1.3;
  }
  .contacts {
    position: absolute;
    left: 32px;
    top: 262px;
    margin: 0;
    padding: 0;
    list-style: none;
    font-size: 19.5px;
    line-height: 1.2;
  }
  .contacts li {
    display: flex;
    align-items: center;
    height: 29px;
  }
  .contacts svg {
    width: 17px;
    height: 17px;
    margin-right: 10px;
    flex: none;
  }
  .front-brand {
    position: absolute;
    right: 34px;
    top: 170px;
    margin: 0;
    width: 250px;
    text-align: right;
    font-size: 42px;
    font-weight: 500;
    line-height: 1.2;
    color: var(--gold);
  }
  .card-back {
    top: 637px;
    background: var(--white);
    display: flex;
    flex-direction: column;
    align-items: center;
    justify-content: center;
  }
  .back-mark {
    width: 150px;
    height: 150px;
    border-radius: 50%;
    background: var(--navy);
    margin-bottom: 26px;
  }
  .back-brand {
    margin: 0;
    font-size: 28px;
    font-weight: 500;
    line-height: 1.2;
    color: var(--navy);
    letter-spacing: 0.5px;
  }
</style>
</head>
<body>
<main class="canvas">
  <section class="card card-front">
    <div class="world-map" role="img" aria-label="Faint world map behind the card details"></div>
    <h1 class="holder-name">Owen Pritchard</h1>
    <p class="holder-title">Managing Director</p>
    <address class="address">14 Harbour Row<br>Cardiff, Wales CF10 4PT</address>
    <ul class="contacts">
      <li>
        <svg viewBox="0 0 16 16" aria-hidden="true"><rect x="4" y="1" width="8" height="14" rx="1.5" fill="var(--icon-gold)"/><rect x="5.5" y="3" width="5" height="8" fill="#17428a"/></svg>
        +44 (0)7382 519 046
      </li>
      <li>
        <svg viewBox="0 0 16 16" aria-hidden="true"><rect x="1" y="3" width="14" height="10" fill="var(--icon-gold)"/><path d="M1 3 L8 9 L15 3" fill="none" stroke="#17428a" stroke-width="1.3"/></svg>
        sales@corvanemotion.co.uk
      </li>
      <li>
        <svg viewBox="0 0 16 16" aria-hidden="true"><circle cx="8" cy="8" r="7" fill="var(--icon-gold)"/><path d="M1 8 H15 M8 1 V15 M3 4.5 H13 M3 11.5 H13" stroke="#17428a" stroke-width="1"/></svg>
        Corvanemotion.co.uk
      </li>
      <li>
        <svg viewBox="0 0 16 16" aria-hidden="true"><rect x="2" y="2" width="12" height="12" fill="var(--icon-gold)"/></svg>
        @motionPostbag
      </li>
      <li>
        <svg viewBox="0 0 16 16" aria-hidden="true"><rect x="2" y="2" width="12" height="12" fill="var(--icon-gold)"/></svg>
        Corvane Motion Limited
      </li>
    </ul>
    <p class="front-brand">Corvane Motion</p>
  </section>

  <section class="card card-back">
    <div class="back-mark" aria-hidden="true"></div>
    <p class="back-brand">Corvane Motion Limited</p>
  </section>
</main>
</body>
</html>
```